Style with Kindness needs a new flyer fast for a giveaway

I am running a contest for the month of December. The woman selected as the winner of the contest will be someone that that has survived a domestic violence situation but would like to kick start in her new life journey. The winner selected will receive 1 month free personal training with a fitness coach 3 times a week, 4 week delivery of smoothies from Leafwhirler and a style consultation and outfit by Celebrity Stylist R.Tasker. All interested candidates should submit a brief personal bio including the reason they should be selected. Submissions are due December 24th and the winner will be selected December 31. Submissions should be sent to stylewithkindnessdallas@mailbox-example.net

Industry/Entity Type

Fashion

Font styles to use
Serif

Colors
886aae
b7a5cd
e4daeb
d2a4cc
b768aa
a64599
e34197
e667a6
eea4c8

Requirements
Must have
• The project has to be worded in a stylish way. I want it is be creative and eye catchy. It also needs to have my style with kindness logo and my Ava P logo on the flyer that I will attach to the brief
Nice to have
• I would like to see different fonts to break up the flyer
Should not have
• It should not just be a paragraph of what I already typed about the contest

```html
<!DOCTYPE html>
<html lang="en">
<head>
<meta charset="utf-8">
<title>Style with Kindness – December Contest Flyer</title>
<link rel="stylesheet" href="https://fonts.googleapis.com/css2?family=Cinzel:wght@400;700&family=Questrial&family=Lustria&family=Alfa+Slab+One&family=Oswald:wght@500;600&family=Didact+Gothic&family=Arimo:wght@700&family=Abril+Fatface&family=Libre+Baskerville&display=swap">
<style>
  :root {
    --violet-deep: #4a1f52;
    --plum: #6e2a6c;
    --lavender: #886aae;
    --lilac: #b7a5cd;
    --mist: #e4daeb;
    --orchid-soft: #d2a4cc;
    --orchid: #b768aa;
    --magenta: #a64599;
    --pink: #e34197;
    --pink-soft: #e667a6;
    --pink-pale: #eea4c8;
    --ink: #1e1b22;
    --slate: #4a4450;
  }
  * { margin: 0; padding: 0; box-sizing: border-box; }
  html, body { width: 848px; height: 1200px; overflow: hidden; background: #fff; }
  .flyer { position: relative; width: 848px; height: 1200px; overflow: hidden; }
  .backdrop {
    position: absolute; inset: 0;
    background:
      radial-gradient(ellipse 260px 340px at 420px 560px, rgba(200,190,200,.55), transparent 70%),
      radial-gradient(ellipse 420px 300px at 760px 260px, rgba(183,165,205,.75), transparent 70%),
      radial-gradient(ellipse 420px 360px at 200px 950px, rgba(210,164,204,.55), transparent 70%),
      radial-gradient(ellipse 380px 300px at 620px 1050px, rgba(136,106,174,.45), transparent 70%),
      linear-gradient(135deg, #ffffff 0%, #f6f1f8 25%, var(--mist) 55%, var(--lilac) 100%);
  }
  .t { position: absolute; white-space: nowrap; line-height: 1; }

  /* headline */
  .eligibility { left: 0; width: 848px; text-align: center; padding-left: 72px; font-family: "Cinzel", serif; color: var(--violet-deep); }
  .eligibility-intro { top: 26px; font-size: 33px; }
  .eligibility-main { top: 50px; font-size: 94px; letter-spacing: 1px; }
  .eligibility-sub { top: 128px; font-size: 41px; color: var(--ink); }

  .prize-lead { left: 244px; width: 400px; text-align: center; font-family: "Questrial", sans-serif; }
  .prize-lead-intro { top: 190px; font-size: 42px; color: var(--ink); }
  .prize-lead-winner { top: 228px; font-size: 98px; color: var(--pink); }
  .prize-lead-note { left: 242px; top: 305px; font-family: "Questrial", sans-serif; font-size: 27px; color: var(--magenta); }
  .prize-lead-journey { left: 249px; top: 328px; font-family: "Questrial", sans-serif; font-size: 55px; color: var(--plum); }

  /* prizes column */
  .prizes-the { left: 26px; top: 466px; transform: rotate(-90deg); transform-origin: left top; font-family: "Lustria", serif; font-size: 30px; color: var(--magenta); }
  .prizes-selected { left: 52px; top: 403px; font-family: "Lustria", serif; font-size: 41px; color: var(--orchid); }
  .prizes-receive { left: 52px; top: 444px; font-family: "Lustria", serif; font-size: 27px; color: var(--orchid); }
  .prizes-month { left: 30px; top: 476px; font-family: "Lustria", serif; font-size: 76px; color: var(--pink); }
  .prizes-training { left: 28px; top: 543px; font-family: "Lustria", serif; font-size: 26px; color: var(--orchid); }
  .prizes-coach { left: 28px; top: 573px; font-family: "Alfa Slab One", serif; font-size: 20px; color: var(--plum); }
  .prizes-times { left: 30px; top: 602px; font-family: "Alfa Slab One", serif; font-size: 56px; color: var(--magenta); }
  .prizes-week { left: 100px; top: 656px; font-family: "Alfa Slab One", serif; font-size: 27px; color: var(--slate); }
  .prizes-delivery-weeks { left: 36px; top: 694px; font-family: "Libre Baskerville", serif; font-size: 58px; color: var(--violet-deep); }
  .prizes-delivery { left: 100px; top: 752px; font-family: "Libre Baskerville", serif; font-size: 29px; color: var(--violet-deep); letter-spacing: 1.5px; }
  .prizes-smoothies { left: 36px; top: 792px; font-family: "Arimo", sans-serif; font-weight: 700; font-size: 26px; color: var(--lavender); }
  .prizes-brand { left: 36px; top: 819px; font-family: "Arimo", sans-serif; font-weight: 700; font-size: 33px; color: var(--magenta); }
  .prizes-and { left: 40px; top: 858px; font-family: "Arimo", sans-serif; font-weight: 700; font-size: 20px; color: var(--ink); }
  .prizes-style-box { position: absolute; left: 37px; top: 881px; width: 303px; height: 46px; background: var(--pink); }
  .prizes-style { left: 44px; top: 888px; font-family: "Arimo", sans-serif; font-weight: 700; font-size: 31px; color: #fff; }
  .prizes-celebrity { left: 42px; top: 938px; font-family: "Arimo", sans-serif; font-weight: 700; font-size: 44px; color: var(--ink); }
  .prizes-stylist { left: 42px; top: 988px; font-family: "Arimo", sans-serif; font-weight: 700; font-size: 40px; color: #5a4a7a; }

  /* entry column */
  .entry-interested { left: 448px; top: 402px; font-family: "Oswald", sans-serif; font-weight: 500; font-size: 52px; color: var(--pink); transform: scaleX(.8); transform-origin: left; }
  .entry-submit { left: 448px; top: 458px; font-family: "Oswald", sans-serif; font-weight: 500; font-size: 39px; color: var(--magenta); transform: scaleX(.82); transform-origin: left; }
  .entry-bio { left: 450px; top: 505px; font-family: "Didact Gothic", sans-serif; font-size: 38px; color: #5d3a6b; letter-spacing: 1px; }
  .entry-reason { left: 450px; top: 550px; font-family: "Didact Gothic", sans-serif; font-size: 30px; color: #5d3a6b; line-height: 30px; }

  .deadline-title { left: 436px; top: 634px; font-family: "Arimo", sans-serif; font-weight: 700; font-size: 48px; color: var(--orchid); }
  .deadline-due { left: 436px; top: 686px; font-family: "Arimo", sans-serif; font-weight: 700; font-size: 38px; color: var(--magenta); }
  .deadline-date { left: 436px; top: 724px; font-family: "Abril Fatface", serif; font-size: 86px; color: #c0307f; }
  .deadline-date sup, .result-date sup { font-size: .42em; vertical-align: top; position: relative; top: .15em; }
  .deadline-month { left: 436px; top: 808px; font-family: "Arimo", sans-serif; font-weight: 700; font-size: 46px; color: var(--magenta); }
  .result-intro { left: 440px; top: 858px; font-family: "Alfa Slab One", serif; font-size: 24px; color: var(--violet-deep); }
  .result-selected { left: 440px; top: 888px; font-family: "Alfa Slab One", serif; font-size: 19px; color: var(--violet-deep); }
  .result-date { left: 440px; top: 914px; font-family: "Libre Baskerville", serif; font-size: 80px; color: var(--violet-deep); letter-spacing: -4px; }
  .result-month { left: 440px; top: 996px; font-family: "Libre Baskerville", serif; font-size: 44px; color: var(--violet-deep); }

  .divider { position: absolute; left: 0; top: 1063px; width: 731px; height: 1px; background: var(--plum); opacity: .7; }

  .brand-mark { left: 70px; top: 1108px; font-family: "Lustria", serif; font-size: 40px; color: var(--plum); }
  .brand-name { left: 420px; top: 1116px; font-family: "Lustria", serif; font-size: 26px; color: var(--plum); }

  .contact-band { position: absolute; left: 731px; top: 694px; width: 117px; height: 506px; background: var(--plum); }
  .contact-text {
    position: absolute; left: 0; top: 0; width: 117px; height: 506px;
    display: flex; flex-direction: column; justify-content: center; align-items: center; gap: 14px;
    writing-mode: vertical-rl; transform: rotate(180deg);
    color: #fff; font-family: "Libre Baskerville", serif; white-space: nowrap; line-height: 1;
  }
  .contact-label { font-size: 21px; }
  .contact-email { font-size: 13px; }
</style>
</head>
<body>
<main class="flyer">
  <div class="backdrop" role="img" aria-label="Soft painted lavender and pink texture with a pair of clasped hands"></div>

  <p class="t eligibility eligibility-intro">The contest is open to</p>
  <h1 class="t eligibility eligibility-main">Domestic</h1>
  <p class="t eligibility eligibility-sub">Violence Survivors</p>

  <p class="t prize-lead prize-lead-intro">A Contest and the</p>
  <h2 class="t prize-lead prize-lead-winner">WINNER</h2>
  <p class="t prize-lead-note">Will Receive a Jump-start on their</p>
  <p class="t prize-lead-journey">New Journey</p>

  <section class="prizes">
    <span class="t prizes-the">The</span>
    <p class="t prizes-selected">Winner Selected</p>
    <p class="t prizes-receive">Will Receive</p>
    <p class="t prizes-month">1 Month</p>
    <p class="t prizes-training">Free Personal Training</p>
    <p class="t prizes-coach">with a Fitness Coach</p>
    <p class="t prizes-times">3 Times</p>
    <p class="t prizes-week">a Week</p>
    <p class="t prizes-delivery-weeks">4 Week</p>
    <p class="t prizes-delivery">Delivery</p>
    <p class="t prizes-smoothies">of smoothies from</p>
    <p class="t prizes-brand">Leafwhirler</p>
    <p class="t prizes-and">and a</p>
    <div class="prizes-style-box"></div>
    <p class="t prizes-style">Style Consultation</p>
    <p class="t prizes-celebrity">by Celebrity</p>
    <p class="t prizes-stylist">Stylist R.Tasker</p>
  </section>

  <section class="entry">
    <p class="t entry-interested">All Interested Should</p>
    <p class="t entry-submit">Submit A Brief Personal</p>
    <p class="t entry-bio">Bio Including the</p>
    <p class="t entry-reason">Reason You Should<br>Be Selected.</p>

    <p class="t deadline-title">Submissions</p>
    <p class="t deadline-due">are due</p>
    <p class="t deadline-date">24<sup>th</sup></p>
    <p class="t deadline-month">December</p>
    <p class="t result-intro">and the Winner</p>
    <p class="t result-selected">will be Selected</p>
    <p class="t result-date">31<sup>th</sup></p>
    <p class="t result-month">December</p>
  </section>

  <div class="divider"></div>
  <p class="t brand-mark">Ava P</p>
  <p class="t brand-name">Style with Kindness</p>

  <aside class="contact-band">
    <div class="contact-text">
      <span class="contact-label">Submissions Should be sent to</span>
      <span class="contact-email">stylewithkindnessdallas@mailbox-example.net</span>
    </div>
  </aside>
</main>
</body>
</html>
```